Business Card Design Project

We need a buisness card for a new digital sinage company. Our target cliants are small to mediaum buisness who want to advertise on out digital sinage network

Target Market(s)

Small to medium buisness

Industry/Entity Type

Digital

Requirements
Must have
• Must have logo

```html
<!DOCTYPE html>
<html lang="en">
<head>
<meta charset="UTF-8">
<title>Signora – Business Card</title>
<link rel="stylesheet" href="https://fonts.googleapis.com/css2?family=Lato:wght@400;700;900&display=swap">
<style>
  :root {
    --backdrop: #66777f;
    --card: #ffffff;
    --blue: #2a8fd6;
    --blue-deep: #2368b4;
    --green: #5a9a2a;
    --orange: #f29a1e;
    --yellow: #f7bd1a;
    --ink: #2b2b2b;
    --ink-soft: #444444;
    --rule: #3a3a3a;
    --wordmark: #4a4a4a;
  }
  * { box-sizing: border-box; margin: 0; padding: 0; }
  html, body {
    width: 1200px;
    height: 960px;
    overflow: hidden;
    background: var(--backdrop);
    font-family: "Lato", Arial, sans-serif;
  }
  .sheet {
    width: 1200px;
    height: 960px;
    display: flex;
    flex-direction: column;
    align-items: center;
    justify-content: center;
    gap: 64px;
  }
  .card {
    position: relative;
    width: 580px;
    height: 330px;
    background: var(--card);
    overflow: hidden;
    box-shadow: 0 10px 24px rgba(0,0,0,0.28);
  }
  .band-top {
    position: absolute;
    top: 0; left: 0; right: 0;
    height: 16px;
    background: linear-gradient(90deg, var(--blue), var(--blue-deep));
  }
  .band-bottom {
    position: absolute;
    bottom: 0; left: 0; right: 0;
    height: 22px;
    background: linear-gradient(90deg, var(--yellow), var(--orange));
  }

  /* Front */
  .identity {
    position: absolute;
    left: 32px;
    top: 48px;
  }
  .person-name {
    font-size: 25px;
    font-weight: 400;
    letter-spacing: 0.3px;
    line-height: 1;
  }
  .person-name .first { color: var(--blue); }
  .person-name .last { color: var(--green); }
  .person-role {
    margin-top: 8px;
    font-size: 16px;
    color: var(--ink-soft);
    letter-spacing: 0.3px;
  }
  .rule {
    position: absolute;
    left: 32px;
    width: 310px;
    height: 1px;
    background: var(--rule);
  }
  .rule.upper { top: 140px; }
  .rule.lower { top: 264px; }
  .contacts {
    position: absolute;
    left: 32px;
    top: 152px;
    list-style: none;
  }
  .contacts li {
    display: flex;
    align-items: center;
    gap: 12px;
    height: 26px;
    font-size: 17px;
    color: var(--ink);
  }
  .contacts li.web { font-weight: 700; }
  .contacts svg { width: 16px; height: 16px; fill: var(--ink); flex: none; }
  .address {
    position: absolute;
    left: 32px;
    top: 276px;
    font-size: 15px;
    color: var(--ink-soft);
  }
  .front-mark {
    position: absolute;
    right: 36px;
    top: 130px;
    display: flex;
    align-items: center;
    gap: 10px;
  }

  /* Shared wordmark */
  .mark-square {
    width: 18px;
    height: 18px;
    background: var(--blue);
  }
  .wordmark {
    font-weight: 900;
    color: var(--wordmark);
    line-height: 1;
  }
  .front-mark .wordmark { font-size: 34px; }

  /* Back */
  .back-mark {
    position: absolute;
    inset: 16px 0 22px 0;
    display: flex;
    align-items: center;
    justify-content: center;
    gap: 16px;
  }
  .back-mark .mark-square { width: 30px; height: 30px; }
  .back-mark .wordmark { font-size: 72px; }
</style>
</head>
<body>
<main class="sheet">

  <section class="card card-front" aria-label="Card front">
    <div class="band-top"></div>

    <div class="identity">
      <h1 class="person-name"><span class="first">LENA</span> <span class="last">MARLOWE</span></h1>
      <p class="person-role">OPERATION MANAGER</p>
    </div>

    <div class="rule upper"></div>
    <ul class="contacts">
      <li>
        <svg viewBox="0 0 16 16" aria-hidden="true"><path d="M2 1h12v14H2z M4 3v3h8V3z M4 8h2v2H4z M7 8h2v2H7z M10 8h2v2h-2z M4 11h2v2H4z M7 11h2v2H7z M10 11h2v2h-2z" fill-rule="evenodd"/></svg>
        (555) 01 234 56 78
      </li>
      <li>
        <svg viewBox="0 0 16 16" aria-hidden="true"><path d="M4 0h8v16H4z M5 2v8h6V2z M7 12h2v2H7z" fill-rule="evenodd"/></svg>
        (555) 09 876 54 32
      </li>
      <li>
        <svg viewBox="0 0 16 16" aria-hidden="true"><path d="M1 3h14v10H1z M2.5 4.5v7h11v-7L8 9z M3.5 4.5L8 7.8l4.5-3.3z" fill-rule="evenodd"/></svg>
        name@signora.com
      </li>
      <li class="web">
        <svg viewBox="0 0 16 16" aria-hidden="true"><circle cx="8" cy="8" r="7.5"/></svg>
        www.signora.com
      </li>
    </ul>
    <div class="rule lower"></div>
    <p class="address">Avenue Lumière, BP 120 - City, Country</p>

    <div class="front-mark">
      <span class="mark-square"></span>
      <span class="wordmark">Signora</span>
    </div>

    <div class="band-bottom"></div>
  </section>

  <section class="card card-back" aria-label="Card back">
    <div class="band-top"></div>
    <div class="back-mark">
      <span class="mark-square"></span>
      <span class="wordmark">Signora</span>
    </div>
    <div class="band-bottom"></div>
  </section>

</main>
</body>
</html>
```